i need a business card design for my family investment company "norvane holdings" based in dubai. its a diverse investment firm focusing on education, hospitality and automotive. the design has to be modern and try to incorporate the logo "E" in the design. details on card as follow

Tariq H Bin Rashoud
Managing Director
tariq@norvane.ae
www.norvane.ae

Harbor park,palmcrest tower, office 1730, dubai
tel. 04 3819025
mobile.050 4172958

Target Market(s)

card used for networking events and investor meetings

Industry/Entity Type

Hospitality

```html
<!DOCTYPE html>
<html lang="en">
<head>
<meta charset="utf-8">
<title>Norvane Holdings – Business Card</title>
<link rel="stylesheet" href="https://fonts.googleapis.com/css2?family=Jost:wght@300;400;600&display=swap">
<style>
  :root {
    --backdrop: #2f2f2f;
    --brand-blue: #44709a;
    --card-white: #ffffff;
    --ink: #1f1f1f;
    --ink-soft: #2b2b2b;
  }
  * { margin: 0; padding: 0; box-sizing: border-box; }
  html, body {
    width: 1200px;
    height: 900px;
    overflow: hidden;
    background: var(--backdrop);
    font-family: "Jost", sans-serif;
  }
  .stage {
    position: relative;
    width: 1200px;
    height: 900px;
  }
  .card {
    position: absolute;
    top: 193px;
    width: 297px;
    height: 513px;
  }
  .card-back {
    left: 288px;
    background: var(--brand-blue);
    display: flex;
    align-items: center;
    justify-content: center;
  }
  .back-wordmark {
    color: var(--card-white);
    font-weight: 300;
    font-size: 26px;
    letter-spacing: 0.32em;
    margin-right: -0.32em;
    text-transform: uppercase;
  }
  .card-front {
    left: 614px;
    background: var(--card-white);
    color: var(--ink);
  }
  .wordmark {
    position: absolute;
    left: 29px;
    top: 30px;
    width: 239px;
    color: var(--ink);
    font-weight: 300;
    text-transform: uppercase;
    line-height: 1;
  }
  .wordmark-name {
    display: block;
    font-size: 38px;
    letter-spacing: 0.22em;
  }
  .wordmark-sub {
    display: block;
    margin-top: 6px;
    font-size: 11px;
    letter-spacing: 1.05em;
  }
  .holder {
    position: absolute;
    left: 29px;
    top: 200px;
  }
  .holder-name {
    font-weight: 600;
    font-size: 14px;
    line-height: 18px;
  }
  .holder-role {
    font-weight: 400;
    font-size: 14px;
    line-height: 20px;
  }
  .divider {
    position: absolute;
    left: 29px;
    width: 111px;
    height: 13px;
    background: var(--brand-blue);
  }
  .divider-1 { top: 246px; }
  .divider-2 { top: 344px; }
  .divider-3 { top: 465px; }
  .details {
    position: absolute;
    left: 29px;
    font-size: 12px;
    line-height: 17.4px;
    color: var(--ink-soft);
    list-style: none;
  }
  .details-contact { top: 290px; }
  .details-address { top: 410px; }
  .label { display: inline-block; width: 12px; }
</style>
</head>
<body>
  <main class="stage">
    <section class="card card-back" aria-label="Card back">
      <span class="back-wordmark">Norvane</span>
    </section>

    <section class="card card-front" aria-label="Card front">
      <h1 class="wordmark">
        <span class="wordmark-name">Norvane</span>
        <span class="wordmark-sub">Holdings</span>
      </h1>

      <div class="holder">
        <p class="holder-name">Tariq H Bin Rashoud</p>
        <p class="holder-role">Managing Director</p>
      </div>
      <div class="divider divider-1"></div>

      <ul class="details details-contact">
        <li><span class="label">P</span> 043 819 025</li>
        <li><span class="label">M</span> 050 417 2958</li>
        <li><span class="label">E</span> tariq@norvane.ae</li>
      </ul>
      <div class="divider divider-2"></div>

      <ul class="details details-address">
        <li>Harbor park,palmcrest tower</li>
        <li>office 1730, dubai</li>
        <li>www.norvane.ae</li>
      </ul>
      <div class="divider divider-3"></div>
    </section>
  </main>
</body>
</html>
```